Redesign of Smart Watch Gift Voucher-SEE ATTACHED CURRENT DESIGN

I need to redesign my existing design using all same content and elements.

MY ENVISION: I invision more of a professional advertisement type of flyer/voucher. Imagine how Corvel.com would create a professionally looking flyer promoting the lumo or veno.

you can get many ideas about professional design by looking at some of corvels flyer designs :
https://www.findora-example.net/search?q=lumo+advertisment&mode=img&ref=a83kd02mzq7

stock photos are attached, you do not have to use them all, you can use some or none i am open to your designs using your own images if you want...just make sure the smartwatch looks black

DO NOT LEAVE ANY CONTENT OR ELEMENTS OUT ON MOCK UP PLEASE

SEE ATTACHED CURRENT DESIGN

I need to redesign my existing design using all same content and elements. DO NOT LEAVE ANY CONTENT OR ELEMENTS OUT ON MOCK UP PLEASE

Target Market(s)

B2B-you can get many ideas about professional design by looking at some of corvels flyer designs :

Industry/Entity Type

Marketing

Requirements
Must have
• I need to redesign my existing design using all same content and elements. DO NOT LEAVE ANY CONTENT OR ELEMENTS OUT ON MOCK UP PLEASE

Nice to have

Should not have

```html
<!DOCTYPE html>
<html lang="en">
<head>
<meta charset="utf-8">
<title>Smartwatch Reward Voucher</title>
<link rel="stylesheet" href="https://fonts.googleapis.com/css2?family=Montserrat:wght@400;500;600;700;800&display=swap">
<style>
  :root {
    --stage: #3a3a3c;
    --card-light: #dedede;
    --card-mid: #cdcdcd;
    --card-edge: #bdbdbd;
    --red: #d0202a;
    --ink: #1b1b1b;
    --body: #2a2a2a;
    --watch-dark: #141414;
    --watch-mid: #2b2b2b;
  }
  * { margin: 0; padding: 0; box-sizing: border-box; }
  html, body {
    width: 972px; height: 1200px; overflow: hidden;
    background: var(--stage);
    font-family: "Montserrat", Arial, sans-serif;
  }
  .voucher {
    position: absolute;
    left: 46px; top: 307px;
    width: 880px; height: 586px;
    background: radial-gradient(ellipse at 50% 40%, var(--card-light) 0%, var(--card-mid) 70%, var(--card-edge) 100%);
    overflow: hidden;
  }
  .watch-photo {
    position: absolute; left: 303px; top: 72px;
    width: 330px; height: 495px;
    border-radius: 95px 95px 70px 70px / 110px 110px 80px 80px;
    background: radial-gradient(ellipse at 50% 40%, var(--watch-mid) 0%, var(--watch-dark) 75%);
    z-index: 1;
  }
  .headline {
    position: absolute; left: 0; top: 0; width: 460px; height: 120px;
    color: var(--red); font-weight: 700; line-height: 1;
    z-index: 2;
  }
  .headline span { position: absolute; white-space: nowrap; }
  .headline .enjoy { left: 37px; top: 28px; font-size: 46px; letter-spacing: -0.3px; }
  .headline .smartwatch { left: 37px; top: 74px; font-size: 43px; letter-spacing: -0.6px; }
  .headline .brand-new { left: 207px; top: 43px; font-size: 16px; color: var(--ink); }
  .tagline {
    position: absolute; left: 39px; top: 121px;
    font-size: 14.8px; font-weight: 600; color: var(--ink); line-height: 17px;
    z-index: 2;
  }
  .copy {
    position: absolute; left: 39px; width: 225px;
    font-size: 9.6px; line-height: 13.2px; color: var(--body);
    text-align: justify;
  }
  .copy.intro { top: 177px; }
  .copy.how { top: 338px; }
  .copy.quote { top: 507px; text-align: left; font-size: 10.4px; line-height: 14.4px; }
  .section-title {
    position: absolute; left: 39px;
    font-size: 14px; font-weight: 700; color: var(--red); line-height: 1;
  }
  .section-title.how-title { top: 311px; }
  .section-title.say-title { top: 486px; }
  .quote-author {
    position: absolute; left: 39px; top: 545px;
    font-size: 10px; font-weight: 700; color: var(--ink);
  }
  .features {
    position: absolute; left: 665px; top: 53px;
    list-style: none;
  }
  .features li {
    display: flex; align-items: center; gap: 12px;
    height: 23.4px;
    font-size: 12.8px; font-weight: 500; color: var(--ink);
  }
  .features svg { width: 10px; height: 12px; flex: none; }
  .redeem {
    position: absolute; left: 665px; top: 354px;
    font-size: 8.5px; line-height: 10.8px; color: var(--ink); text-transform: uppercase;
  }
  .redeem .site { display: block; text-transform: none; font-weight: 700; font-size: 11.1px; line-height: 13px; }
  .redeem .terms { display: block; text-transform: none; font-size: 7.5px; margin-top: 1px; }
  .meta-label, .meta-value { position: absolute; left: 665px; font-size: 15.2px; font-weight: 700; line-height: 1; }
  .meta-label { color: var(--ink); }
  .meta-value { color: var(--red); }
  .cert-label { top: 429px; }
  .cert-value { top: 449px; }
  .exp-label { top: 489px; }
  .exp-value { top: 509px; }
</style>
</head>
<body>
  <section class="voucher">
    <div class="watch-photo" role="img" aria-label="Photo of a black square smartwatch showing colourful app tiles on its screen"></div>

    <h1 class="headline">
      <span class="enjoy">ENJOY</span>
      <span class="brand-new">YOUR BRAND NEW</span>
      <span class="smartwatch">SMARTWATCH</span>
    </h1>
    <p class="tagline">Take control of your life with<br>Your new smart fitness watch</p>

    <p class="copy intro">Congratulations, you have been rewarded with a Brand New Smart Fitness Watch shipped right to your door. Just pay shipping and handling. Your new Smart Fitness Watch has these features: sport mode, pedometer, distance, calorie, heart rate, blood pressure, stopwatch, sleep monitoring, phone locator, reminders, remote camera, an alarm clock and much more!</p>

    <h2 class="section-title how-title">HOW CAN WE DO THIS</h2>
    <p class="copy how">We have a couple retail partners that we team up with to "crowd purchase" huge shipping containers that hold 10's of thousands of electronic products at 80-90% off retail. We simply pass our savings on to you as we do not profit from our electronic products. You are basically able to "piggy back" on our partner-ships and buying power to get an attractive electronic premium for a fraction of the retail cost.</p>

    <h2 class="section-title say-title">WHAT OTHERS SAY</h2>
    <p class="copy quote">"Are you sure this is not a Norvik Stellar Smartwatch in DISGUISE???? I love mine."</p>
    <p class="quote-author">Corin T. Bayview, NJ</p>

    <ul class="features">
      <li><svg viewBox="0 0 10 12"><circle cx="5" cy="6" r="3.6" fill="none" stroke="#d0202a" stroke-width="1.6"/></svg>Pedomoter</li>
      <li><svg viewBox="0 0 10 12"><circle cx="5" cy="6" r="3.6" fill="none" stroke="#d0202a" stroke-width="1.6"/></svg>Distance Tracker</li>
      <li><svg viewBox="0 0 10 12"><circle cx="5" cy="6" r="3.6" fill="none" stroke="#d0202a" stroke-width="1.6"/></svg>Calorie Counter</li>
      <li><svg viewBox="0 0 10 12"><circle cx="5" cy="6" r="3.6" fill="none" stroke="#d0202a" stroke-width="1.6"/></svg>Heart Rate Monitor</li>
      <li><svg viewBox="0 0 10 12"><circle cx="5" cy="6" r="3.6" fill="none" stroke="#d0202a" stroke-width="1.6"/></svg>Blood Pressure Monitor</li>
      <li><svg viewBox="0 0 10 12"><circle cx="5" cy="6" r="3.6" fill="none" stroke="#d0202a" stroke-width="1.6"/></svg>Stopwatch</li>
      <li><svg viewBox="0 0 10 12"><circle cx="5" cy="6" r="3.6" fill="none" stroke="#d0202a" stroke-width="1.6"/></svg>Sleep Monitoring</li>
      <li><svg viewBox="0 0 10 12"><circle cx="5" cy="6" r="3.6" fill="none" stroke="#d0202a" stroke-width="1.6"/></svg>Phone Locator</li>
      <li><svg viewBox="0 0 10 12"><circle cx="5" cy="6" r="3.6" fill="none" stroke="#d0202a" stroke-width="1.6"/></svg>Reminders Feature</li>
      <li><svg viewBox="0 0 10 12"><circle cx="5" cy="6" r="3.6" fill="none" stroke="#d0202a" stroke-width="1.6"/></svg>Remote Camera</li>
      <li><svg viewBox="0 0 10 12"><circle cx="5" cy="6" r="3.6" fill="none" stroke="#d0202a" stroke-width="1.6"/></svg>Alarm Clock</li>
      <li><svg viewBox="0 0 10 12"><circle cx="5" cy="6" r="3.6" fill="none" stroke="#d0202a" stroke-width="1.6"/></svg>Waterproof</li>
    </ul>

    <p class="redeem">View all the details of this<br>special offer and redeem online at:
      <span class="site">www.perksandrewardsclub.com</span>
      <span class="terms">*Terms and Conditions apply see website for details</span>
    </p>

    <p class="meta-label cert-label">CERTIFICATE ID:</p>
    <p class="meta-value cert-value">91772-89218</p>
    <p class="meta-label exp-label">EXPIRES:</p>
    <p class="meta-value exp-value">10/03/2020</p>
  </section>
</body>
</html>
```